Need a new Website Design

We are changing the project requirements because we did not get desired design. Here are the new requirements.

We sell machinery used to compact recyclable materials into neat and tidy bales. We also sell accessories and consumables related this equipment.

Our existing website is:
http://www.trenvopak.com

Our company name is 'Kelworth Trenvopak Machinery co. LTD' and we only need 1 page designed creatively. The homepage should introduce our company and what we do, as well as direct them to search or browse our balers and baler related products. It should also exude a sense of credibility, confidence and success.

Important Notes:
Links to the logo files:
- Adobe Illustrator format: http://www.trenvopak.com/assets/Trenvopak.ai
- Corel Draw format: http://www.trenvopak.com/assets/Trenvopak.cdr

Links to the Trenvopak proprietary font:
- Adobe Illustrator format: http://www.trenvopak.com/assets/Trenvopak-font.ai
- Corel Draw format: http://www.trenvopak.com/assets/Trenvopak-font.cdr

Our marketing photos can be downloaded here: http://qlinkr.example/PmQ7tR
You can see an example of the homepage on http://www.trenvopak.com/home-test/
Proprietary images are available here: http://www.snapvault.example/photos/48103977@K07/

It is important that the user should be able to access his needed baler either by type (vertical/horizontal baler) or applications straight from the homepage.

Important:
one general comment which I should have brought up from the beginning is that google analytics shows that most clients go about doing their business on our site by clicking on baler types, vertical balers, horizontal balers, and waste applications. They either want to see the whole product range first, or they already set on a manual or vertical baler, or they have no idea and thus prefer to browse the waste applications to pin down the type of waste they have have that needs to be baled. It would be good to have all of our balers and applications listed in the home page. This is one way to do it but by no means is it the right way:

http://www.trenvopak.com/home-test/

Target Market(s)

Industrial

Industry/Entity Type

Marketing

Requirements
Must have
• The logo and machine colors should be used for the color scheme. It must appeal to an international and eclectic market of recyclers, traders and small businesses. Other than that it should look and feel authentic.
Nice to have
• N/A
Should not have
• N/A

```html
<!DOCTYPE html>
<html lang="en">
<head>
<meta charset="utf-8">
<title>Trenvopak – Your Baling Solution</title>
<link href="https://fonts.googleapis.com/css2?family=Ropa+Sans&family=Roboto:wght@300;400;700&display=swap" rel="stylesheet">
<style>
:root{
  --blue:#1a72b8;
  --blue-dark:#125d99;
  --blue-light:#2b8ad0;
  --lime:#b5cf2d;
  --lime-dark:#9dba1c;
  --ink:#444;
  --muted:#666;
  --line:#dcdfe2;
  --page:#f3f5f6;
  --white:#fff;
}
*{box-sizing:border-box;margin:0;padding:0}
html,body{width:1200px;height:960px;overflow:hidden}
body{background:var(--page);font-family:"Roboto",sans-serif;font-weight:300;color:var(--ink);position:relative}
a{color:inherit;text-decoration:none}
.heading{font-family:"Ropa Sans",sans-serif;font-weight:400}

.topbar{position:absolute;top:0;left:0;width:1200px;height:20px}
.social{position:absolute;display:flex;gap:3px}
.social span{width:13px;height:13px;border-radius:2px;display:block}
.social .s1{background:#c8302a}.social .s2{background:#3aa6dc}.social .s3{background:#3b5b99}
.topbar .social{left:414px;top:5px}
.toplinks{position:absolute;right:200px;top:0;display:flex;font-family:"Ropa Sans",sans-serif;font-size:11px;color:#555;letter-spacing:.5px}
.toplinks a{padding:3px 10px 0;height:19px;border-left:1px solid var(--line)}
.toplinks a:last-child{border-right:1px solid var(--line)}
.toplinks .lang::after{content:"";display:inline-block;margin-left:6px;border:4px solid transparent;border-top:5px solid #555;vertical-align:-2px}

.navband{position:absolute;top:20px;left:0;width:1200px;height:33px;background:linear-gradient(#2a84c8,#1566a9);border-bottom:1px solid #0e5289}
.nav{position:absolute;left:437px;top:7px;display:flex;gap:0;font-family:"Ropa Sans",sans-serif;font-size:11.5px;color:var(--white);letter-spacing:.6px}
.nav a{padding:2px 6px 0;height:19px;margin-right:11px}
.nav a.active{background:#3c97da}

.logo{position:absolute;left:199px;top:4px;width:212px;height:64px;background:var(--white);border:1px solid #c9ccce;display:flex;flex-direction:column;justify-content:center;padding-left:20px}
.logo .name{font-family:"Roboto",sans-serif;font-weight:400;font-size:25px;color:#333;letter-spacing:.5px;line-height:1}
.logo .tag{font-family:"Roboto",sans-serif;font-weight:400;font-size:6.5px;color:#333;margin:3px 0 0 74px;letter-spacing:.3px}

.hero{position:absolute;left:199px;top:53px;width:800px;height:255px;background:linear-gradient(120deg,#8a6a45 0%,#c8893e 25%,#a87b4a 45%,#2f6ea8 65%,#3a4450 100%)}
.hero::after{content:"";position:absolute;left:0;right:0;bottom:0;height:56px;background:linear-gradient(rgba(255,255,255,0),rgba(255,255,255,.45))}
.hero .caption{position:absolute;left:12px;bottom:9px;z-index:1;font-family:Arial,sans-serif}
.hero .caption b{display:block;font-size:18px;color:#1c4f82;line-height:1}
.hero .caption span{font-size:15px;color:#28435e}

.tabs{position:absolute;left:199px;top:308px;width:800px;height:32px;display:flex;font-family:"Ropa Sans",sans-serif;font-size:14px;letter-spacing:1px}
.tabs a{flex:1;display:flex;align-items:center;justify-content:center;color:var(--white);background:linear-gradient(#2482c6,#1866a8);border-left:1px solid #4d9bd4}
.tabs a.current{background:linear-gradient(var(--lime),var(--lime-dark));color:#333;border-left:0}

.welcome{position:absolute;left:199px;top:357px;width:593px}
.welcome h1{font-size:17px;color:#444;margin-top:0;font-weight:400;letter-spacing:.3px}
.download{position:absolute;left:406px;top:0;width:187px;height:31px;background:linear-gradient(#2482c6,#1866a8);color:var(--white);font-family:"Ropa Sans",sans-serif;font-size:12px;display:flex;align-items:center;padding-left:8px;gap:6px}
.intro{margin-top:16px;font-size:10px;line-height:16px;color:var(--muted)}
.intro .photo{float:left;width:128px;height:64px;margin:1px 13px 0 1px;background:linear-gradient(#9fb9d6,#e4e8ec 60%,#8a96a3)}
.intro p+p{margin-top:16px}
.more{display:inline-flex;align-items:center;gap:6px;font-family:"Ropa Sans",sans-serif;font-size:10px;color:#555;font-weight:400;margin-top:6px}
.more i{width:11px;height:11px;border-radius:50%;background:#3d3d3d;display:inline-flex;align-items:center;justify-content:center}
.more.hot{color:var(--blue)}.more.hot i{background:var(--blue)}

.rule{position:absolute;left:199px;width:593px;border-top:1px dashed #cfd3d6}
.cards{position:absolute;left:199px;top:613px;width:593px;display:flex;justify-content:space-between}
.card{width:190px}
.card h2{font-size:14px;color:var(--blue);font-weight:400;margin-left:0}
.card .img{width:186px;height:104px;margin:6px 0 10px 1px}
.card p{font-size:10px;line-height:13px;color:var(--muted)}
.card .more{margin-top:7px;margin-left:1px}

.bigbtns{position:absolute;left:200px;top:833px;width:592px;display:flex;gap:4px;height:47px}
.bigbtns a{display:flex;align-items:center;justify-content:center;color:var(--white);background:linear-gradient(#2482c6,#1765a6);font-family:"Ropa Sans",sans-serif;font-size:14px;letter-spacing:.4px}

.side{position:absolute;left:808px;top:357px;width:192px}
.side h3{height:31px;background:linear-gradient(var(--lime),var(--lime-dark));color:var(--blue);font-size:17px;padding-left:10px;display:flex;align-items:center;justify-content:space-between;padding-right:7px}
.side h3 i{width:14px;height:14px;border-radius:50%;background:var(--blue);display:flex;align-items:center;justify-content:center}
.side ul{list-style:none;margin-top:5px}
.side li{font-size:10px;color:#555;padding:4px 5px 5px;border-bottom:1px solid var(--line);line-height:12px}

.footer{position:absolute;left:199px;top:903px;width:800px;border-top:1px solid #d0d4d7;padding-top:10px}
.footer nav{font-family:"Ropa Sans",sans-serif;font-size:10.5px;color:#777;letter-spacing:.3px}
.footer nav span{margin:0 7px;color:#999}
.footer small{display:block;font-size:8.5px;color:#888;margin-top:6px;font-family:"Ropa Sans",sans-serif;letter-spacing:.3px}
.footer .social{right:0;top:16px}
</style>
</head>
<body>
<header>
  <div class="topbar">
    <div class="social"><span class="s1"></span><span class="s2"></span><span class="s3"></span></div>
    <nav class="toplinks"><a>Track your order</a><a>Technical Support</a><a>Contact us</a><a class="lang">Language</a></nav>
  </div>
  <div class="navband">
    <nav class="nav"><a class="active">Home</a><a>About us</a><a>Baler Types</a><a>Applications</a><a>Baler Accessories</a><a>Testimonials</a><a>Inquire Now!</a></nav>
  </div>
  <div class="logo"><span class="name">TRENVOPAK</span><span class="tag">YOUR BALING SOLUTION.</span></div>
</header>

<section class="hero" role="img" aria-label="Blue baling press compacting straw bales in a factory hall, two workers beside it">
  <div class="caption"><b>LOREM IPSUM IS SIMPLY</b><span>text of the printing and typesetting industry.</span></div>
</section>
<nav class="tabs"><a class="current">Vertical Balers</a><a>Horizontal Balers</a><a>Customized Balers</a></nav>

<main>
  <section class="welcome">
    <h1 class="heading">Welcome to Trenvopak</h1>
    <a class="download">
      <svg width="18" height="22" viewBox="0 0 18 22"><path d="M1 1h11l5 5v15H1z" fill="#fff"/><path d="M12 1v5h5" fill="#ddd"/><rect x="0" y="3" width="9" height="5" fill="#d33"/><path d="M4 17c3-6 5-8 5-10s-2-1-1 2 4 6 6 6-2-2-5-1-5 3-5 3z" fill="none" stroke="#d33" stroke-width="1"/></svg>
      Download Product Catlogue
    </a>
    <div class="intro">
      <div class="photo" role="img" aria-label="Trenvopak factory building exterior"></div>
      <p>Trenvopak, a pioneer baler manufacturer, supplies industry-leading and cost-effective baling solutions for all types of waste material. From small standalone vertical presses to fully automated horizontal lines, we offer a complete range of baling machinery. Our smartly designed machines are CE certified, with top brand hydraulics and electric components. Durability and affordable prices make our machinery stands out among similar baling presses. As a pioneer in the waste recycling market, we help you turn your waste into a new source of profit.</p>
      <p>Be ready to witness large savings on recycling and waste removal costs. Trenvopak waste specialists work around the hour and across the globe to bring you considerate after-sales service, strict quality standards and long term value for your most challenging waste handling projects.</p>
    </div>
    <a class="more">Know more <i><svg width="6" height="7"><path d="M1 0l4 3.5L1 7" fill="none" stroke="#fff" stroke-width="1.5"/></svg></i></a>
  </section>

  <div class="rule" style="top:599px"></div>

  <section class="cards">
    <article class="card">
      <h2 class="heading">Lorem Ipsum is simply</h2>
      <div class="img" role="img" aria-label="Blue horizontal baler with conveyor" style="background:linear-gradient(#5a6a78,#2c92d4 55%,#4a4f55)"></div>
      <p>Durability and affordable prices make our machinery stands out among.</p>
      <a class="more">Know more <i><svg width="6" height="7"><path d="M1 0l4 3.5L1 7" fill="none" stroke="#fff" stroke-width="1.5"/></svg></i></a>
    </article>
    <article class="card">
      <h2 class="heading">Lorem Ipsum is simply</h2>
      <div class="img" role="img" aria-label="Technician presenting a yellow baler" style="background:linear-gradient(90deg,#3d4a66 0%,#e3a51c 35%,#f0b52a 75%,#2a6aa8)"></div>
      <p>Durability and affordable prices make our machinery stands out among.</p>
      <a class="more hot">Know more <i><svg width="6" height="7"><path d="M1 0l4 3.5L1 7" fill="none" stroke="#fff" stroke-width="1.5"/></svg></i></a>
    </article>
    <article class="card">
      <h2 class="heading">Lorem Ipsum is simply</h2>
      <div class="img" role="img" aria-label="Vertical blue baler in a workshop" style="background:linear-gradient(#8f9aa3,#39a3d6 50%,#55606a)"></div>
      <p>Durability and affordable prices make our machinery stands out among.</p>
      <a class="more">Know more <i><svg width="6" height="7"><path d="M1 0l4 3.5L1 7" fill="none" stroke="#fff" stroke-width="1.5"/></svg></i></a>
    </article>
  </section>

  <div class="rule" style="top:812px"></div>

  <nav class="bigbtns">
    <a style="width:203px">How Can We Help You</a>
    <a style="width:194px">Why Choose Us</a>
    <a style="width:187px">Product Gallery</a>
  </nav>
</main>

<aside class="side">
  <h3 class="heading">Applications <i><svg width="8" height="6"><path d="M1 1l3 3 3-3" fill="none" stroke="#fff" stroke-width="1.6"/></svg></i></h3>
  <ul>
    <li>Aluminum Alloy Frame/Sheet</li>
    <li>Aluminum Can Baling</li>
    <li>Cardboard Baler (e.g. OCC, Carton)</li>
    <li>Chopped Straw/Hay</li>
    <li>Cotton Seed</li>
    <li>Disposable Tableware</li>
    <li>Drum/Barrel (e.g. Paint Drum, Oil Barrel)</li>
    <li>Foam (Sponge)</li>
    <li>Hollow Plastic (e.g. PET Bottle, PP Container, PVC Pipe, HDPE/PP Jar)</li>
    <li>Leaves</li>
    <li>Mineral Cotton Fiber (Asbestus)</li>
    <li>Natural Fiber (e.g. Coconut Fiber, Palm Fiber, Abaca Fiber, Wool, Cotton)</li>
    <li>Paper (e.g. OMG, ONP, Book, Craft Paper, Paper Trim, Paper Waste)</li>
    <li>Peanut Shell</li>
    <li>Plastic Shell (e.g. Computer Shell, Car Bumper, TV Shell)</li>
    <li>Rice Husk</li>
    <li style="border-bottom:0">Sawdust</li>
  </ul>
</aside>

<footer class="footer">
  <nav>Home<span>|</span>About us<span>|</span>Baler Types<span>|</span>Baler Applications<span>|</span>Baler Accessories<span>|</span>Baler News<span>|</span>Baler Gallery<span>|</span>Contact Us</nav>
  <small>© 2013 Trenvopak Machinery Company Limited. All Rights Reserved.</small>
  <div class="social"><span class="s1"></span><span class="s2"></span><span class="s3"></span></div>
</footer>
</body>
</html>
```